VORELA poster design that will include information about our project / product

We need a nice design for our poster (VORELA project poster). The content is presented in the attached doc file. With yellow are some instructions. We need a professional design for a European Project. <br/>I attach the logos of the Consortium that should be placed in the right order inside the Poster at the appropriate section (I attach the photos in different formats - you can use whichever logo is more convenient). I also attach the high-quality logo of VORELA.

Target Market(s)

Policy Makers, Health professionals

Industry/Entity Type

Health And Wellness

Font styles to use
Serif
Sans Serif

Colors
2f74b4
0255a3
33a6d7
ffcf3e
ffc214

Requirements
Must have
• - professional design
• - modern design
• - colors relevant to the logo
Nice to have
• Proposed size 80cm wide to 200cm height.

```html
<!DOCTYPE html>
<html lang="en">
<head>
<meta charset="utf-8">
<title>VORELA – Tinnitus Patients Poster</title>
<link href="https://fonts.googleapis.com/css2?family=Montserrat:wght@400;600;700;800;900&family=Open+Sans:wght@400;600;700&display=swap" rel="stylesheet">
<style>
:root{
  --blue:#0255a3;
  --blue-mid:#2f74b4;
  --sky:#33a6d7;
  --navy:#0b3f80;
  --band:#0d4d96;
  --yellow:#ffc214;
  --yellow-soft:#ffcf3e;
  --grey:#e8edf3;
  --ink:#1f2d3d;
  --white:#ffffff;
}
*{box-sizing:border-box;margin:0;padding:0}
html,body{width:1200px;height:2976px;overflow:hidden;background:var(--white)}
body{font-family:"Open Sans",Arial,sans-serif;color:var(--ink);position:relative}
.head{font-family:"Montserrat",Arial,sans-serif}

.brand{position:absolute;left:470px;top:30px;width:260px;height:260px;border-radius:50%;background:var(--blue);
  display:flex;align-items:center;justify-content:center;color:var(--white);font-family:"Montserrat",sans-serif;font-weight:800;font-size:52px;letter-spacing:4px}

.title-band{position:absolute;left:0;top:420px;width:1200px;height:270px;background:var(--grey);text-align:center}
.title-band .kicker{font-family:"Montserrat",sans-serif;font-weight:800;color:var(--blue);font-size:33px;padding-top:44px;letter-spacing:.5px}
.title-band .main{font-family:"Montserrat",sans-serif;font-weight:900;color:var(--blue);font-size:104px;line-height:1;margin-top:34px;letter-spacing:2px}

.rationale{position:absolute;left:0;top:745px;width:1200px;text-align:center}
.rationale h2{font-family:"Montserrat",sans-serif;font-weight:800;color:var(--blue);font-size:54px;line-height:1.05}
.rationale h2 span{display:block;color:var(--yellow);font-size:66px}
.rationale .copy{width:1060px;margin:40px auto 0;text-align:left}
.rationale p{font-size:21px;line-height:1.45;margin-bottom:24px;color:#2a3544}

.dss{position:absolute;left:0;top:1345px;width:1200px;height:530px}
.dss-caption{position:absolute;left:260px;top:0;width:700px;text-align:center;font-family:"Montserrat",sans-serif;font-weight:700;color:var(--blue);font-size:22px;letter-spacing:3px}
.dss-caption .mini{display:block;margin:0 auto 8px;width:56px;height:56px;border-radius:50%;border:4px solid var(--blue)}
.patients{position:absolute;left:40px;top:40px;width:200px}
.patient{display:flex;align-items:center;height:60px;font-size:15px;font-weight:700;color:var(--blue)}
.patient i{width:34px;height:34px;border-radius:50%;background:var(--sky);margin-right:12px;flex:none}
.patient.dots{padding-left:46px;font-size:26px;line-height:1}
.dss-frame{position:absolute;left:262px;top:105px;width:700px;height:420px;background:var(--blue);border-radius:22px;padding:22px}
.panel{position:absolute;background:var(--white);border-radius:14px;padding:16px}
.panel h3{font-family:"Montserrat",sans-serif;font-weight:800;color:var(--blue);font-size:28px;margin-bottom:10px}
.panel.input{left:22px;top:22px;width:250px;height:376px}
.panel.core{left:292px;top:22px;width:170px;height:376px;background:var(--sky);color:var(--white);text-align:center}
.panel.core h3{color:var(--white)}
.panel.output{left:482px;top:22px;width:196px;height:376px}
.panel ul{list-style:none}
.panel li{font-size:16px;font-weight:600;padding:8px 0 8px 22px;position:relative;color:var(--blue)}
.panel li::before{content:"";position:absolute;left:0;top:14px;width:11px;height:11px;border-radius:50%;background:var(--yellow)}
.core .chip{background:var(--white);color:var(--blue);font-weight:700;font-size:15px;border-radius:8px;padding:10px 6px;margin:16px 0}
.treatments{position:absolute;left:995px;top:40px;width:180px}
.treat{height:33px;display:flex;align-items:center;font-size:15px;font-weight:700;color:var(--blue)}
.treat::before{content:"";width:28px;height:2px;background:var(--blue);margin-right:10px}

.method{position:absolute;left:0;top:1905px;width:1200px;height:700px;background:var(--band);color:var(--white)}
.method h2{font-family:"Montserrat",sans-serif;font-weight:800;font-size:56px;text-align:center;padding-top:24px;letter-spacing:2px}
.layer{position:absolute;left:40px;width:720px}
.layer .tag{display:inline-block;background:var(--white);color:var(--band);font-family:"Montserrat",sans-serif;font-weight:800;font-size:14px;padding:4px 12px;border-radius:4px}
.layer .row{display:flex;justify-content:space-between;margin-top:16px}
.step{width:80px;text-align:center;font-size:11px;line-height:1.2;font-weight:600}
.step i{display:block;width:50px;height:50px;margin:0 auto 8px;border-radius:50%;border:3px solid var(--white)}
.layer .bar{margin-top:14px;border-top:2px solid var(--sky);padding-top:6px;font-size:12px;color:#cfe1f5}
.notes{position:absolute;left:800px;width:370px}
.notes h3{font-family:"Montserrat",sans-serif;font-weight:800;color:var(--yellow);font-size:24px;margin-bottom:8px}
.notes p{font-size:16px;line-height:1.4}
.refs{position:absolute;left:800px;top:580px;width:370px;font-size:11px;color:#cfe1f5;line-height:1.5}

.consortium{position:absolute;left:0;top:2605px;width:1200px;height:195px;text-align:center}
.consortium h2{font-family:"Montserrat",sans-serif;font-weight:800;color:var(--blue);font-size:44px;padding-top:12px}
.partners{display:flex;flex-wrap:wrap;justify-content:center;gap:14px 22px;margin-top:14px;padding:0 40px}
.partner{width:110px;height:44px;border-radius:8px;background:#d6e2ef}

.contacts{position:absolute;left:0;top:2800px;width:1200px;height:140px;background:var(--navy);color:var(--white)}
.contacts h2{position:absolute;left:420px;top:18px;font-family:"Montserrat",sans-serif;font-weight:800;font-size:26px}
.contacts .lines{position:absolute;left:420px;top:60px;font-size:14px;line-height:1.55}
.contacts .lines b{display:inline-block;width:10px;height:10px;border-radius:50%;background:var(--sky);margin-right:8px}
.facts{position:absolute;left:880px;top:18px;width:300px;font-size:12px;line-height:1.5}
.facts h3{font-family:"Montserrat",sans-serif;font-weight:800;font-size:16px;margin-bottom:4px}
.facts strong{color:var(--yellow-soft)}

.footer{position:absolute;left:0;top:2940px;width:1200px;height:36px;display:flex;align-items:center;padding-left:60px;font-size:13px;color:#3a4656}
.footer i{width:42px;height:28px;background:var(--blue);margin-right:14px}
</style>
</head>
<body>

<div class="brand">VORELA</div>

<section class="title-band">
  <div class="kicker">UNIFICATION OF TREATMENTS AND INTERVENTIONS FOR</div>
  <div class="main">TINNITUS PATIENTS</div>
</section>

<section class="rationale">
  <h2>RATIONALE AND<span>OBJECTIVES</span></h2>
  <div class="copy">
    <p>Tinnitus consists of the perception of a phantom sound including the patient's reaction to it. Tinnitus remains a scientific and clinical enigma of immensely high prevalence and socio-economic burden.</p>
    <p>The overall aim of the VORELA project is to deliver a predictive computational model based on existing and longitudinal data attempting to address the question, which tinnitus treatment approach is optimal for a specific patient group based on specific parameters.</p>
    <p>Clinical, epidemiological, medical, genetic and audiological data, including signals reflecting ear-brain communication, will be analysed from existing databases. Predictive factors for different patient groups will be extracted and their prognostic relevance will be validated in a randomized controlled trial (RCT) in which different groups of patients will undergo a combination of therapies targeting both auditory and central nervous.</p>
  </div>
</section>

<section class="dss">
  <div class="dss-caption"><span class="mini"></span>DECISION | SUPPORT | SYSTEM</div>
  <div class="patients">
    <div class="patient"><i></i>PATIENT 1</div>
    <div class="patient"><i></i>PATIENT 2</div>
    <div class="patient"><i></i>PATIENT 3</div>
    <div class="patient dots">⋮</div>
    <div class="patient"><i></i>PATIENT 4</div>
    <div class="patient dots">⋮</div>
    <div class="patient"><i></i>PATIENT 5</div>
    <div class="patient"><i></i>PATIENT 15,000</div>
  </div>
  <div class="dss-frame">
    <div class="panel input">
      <h3>INPUT</h3>
      <ul>
        <li>Genetic data</li>
        <li>Electrophysiological data</li>
        <li>Tinnitus characteristics</li>
        <li>Medical history</li>
        <li>Epidemiological data</li>
        <li>Questionnaires</li>
      </ul>
    </div>
    <div class="panel core">
      <h3>VORELA</h3>
      <div style="font-weight:800;font-size:22px">DSS</div>
      <div class="chip">Feature extraction</div>
      <div class="chip">Model training</div>
      <div class="chip">AI model</div>
    </div>
    <div class="panel output">
      <h3>OUTPUT</h3>
      <ul>
        <li>Personalised set of examinations</li>
        <li>Optimal treatment</li>
      </ul>
    </div>
  </div>
  <div class="treatments">
    <div class="treat">Treatment 1</div>
    <div class="treat">Treatment 2</div>
    <div class="treat">Treatment 3</div>
    <div class="treat">Treatment 4</div>
    <div class="treat">T1+T2</div>
    <div class="treat">T1+T3</div>
    <div class="treat">T1+T4</div>
    <div class="treat">T2+T3</div>
    <div class="treat">T2+T4</div>
    <div class="treat">T1+T2+T3</div>
    <div class="treat">T1+T2+T4</div>
    <div class="treat">T1+T2+T3+T4</div>
  </div>
</section>

<section class="method">
  <h2>METHODOLOGY</h2>

  <div class="layer" style="top:110px">
    <span class="tag">LAYER 1</span>
    <div class="row">
      <div class="step"><i></i>Clinical data</div>
      <div class="step"><i></i>Epidemiological data</div>
      <div class="step"><i></i>Genetic data</div>
      <div class="step"><i></i>Audiological data</div>
      <div class="step"><i></i>Factors linked to outcome</div>
      <div class="step"><i></i>Big data analysis</div>
      <div class="step"><i></i>Subgroup profiles</div>
      <div class="step"><i></i>Prognostic markers</div>
    </div>
    <div class="bar">Pre-analysis of existing databases</div>
  </div>

  <div class="layer" style="top:290px">
    <span class="tag">LAYER 2</span>
    <div class="row">
      <div class="step"><i></i>500 patients</div>
      <div class="step"><i></i>Patient randomization</div>
      <div class="step"><i></i>Single treatment</div>
      <div class="step"><i></i>Combined treatment</div>
      <div class="step"><i></i>Follow-up visits</div>
      <div class="step"><i></i>Outcome evaluation</div>
    </div>
    <div class="bar">Randomized clinical trial across five sites</div>
  </div>

  <div class="layer" style="top:470px">
    <span class="tag">LAYER 3</span>
    <div class="row">
      <div class="step"><i></i>In silico model</div>
      <div class="step"><i></i>Data integration</div>
      <div class="step"><i></i>Model validation</div>
      <div class="step"><i></i>Treatment suggestion</div>
      <div class="step"><i></i>Clinical use</div>
    </div>
    <div class="bar">Development of the decision support system</div>
  </div>

  <div class="notes" style="top:130px">
    <h3>ANALYSIS OF EXISTING DATA</h3>
    <p>Factors correlating to treatment outcome<br>Genetic markers<br>Blood biomarkers</p>
  </div>
  <div class="notes" style="top:300px">
    <h3>COLLECTION OF NEW DATA</h3>
    <p>500 Patients, 5 Centers<br>4 different treatments<br>Single treatments and combination</p>
  </div>
  <div class="notes" style="top:450px">
    <h3>DEVELOPMENT OF DSS</h3>
    <p>In silico model<br>Suggestion of additional assessments<br>Suggestion of optimal treatment</p>
  </div>
  <div class="refs">1 Clinical outcome study, 2019<br>2 Audiology review, 2020<br>3 Treatment cohort report, 2018</div>
</section>

<section class="consortium">
  <h2>CONSORTIUM</h2>
  <div class="partners" aria-label="Partner badges">
    <div class="partner"></div><div class="partner"></div><div class="partner"></div><div class="partner"></div>
    <div class="partner"></div><div class="partner"></div><div class="partner"></div><div class="partner"></div>
    <div class="partner"></div><div class="partner"></div><div class="partner"></div><div class="partner"></div>
    <div class="partner"></div><div class="partner"></div><div class="partner"></div><div class="partner"></div>
  </div>
</section>

<section class="contacts">
  <h2>CONTACTS</h2>
  <div class="lines">
    <div><b></b>www.vorela-project.eu</div>
    <div><b></b>@vorela_project</div>
    <div><b></b>info@vorela-project.eu</div>
  </div>
  <div class="facts">
    <h3>KEY FACTS</h3>
    <div><strong>STARTING DATE:</strong> 01.01.2020</div>
    <div><strong>DURATION:</strong> 48 months</div>
    <div><strong>EU CONTRIBUTION:</strong> €5.9M</div>
    <div><strong>PROJECT COORDINATOR:</strong> Vorela Research Unit</div>
  </div>
</section>

<footer class="footer"><i></i>This project has received funding from the European Union's Framework Research Programme under grant agreement.</footer>

</body>
</html>
```